Top Producing Realtor Business Card Design

Looking for branding with my logo on all of my materials. I am a top producing real estate agent, selling expensive homes in California. I'm looking for a classy design that includes my existing logo, the company corporate logo and my photo.

Looking forward to your submissions! Thank you so much! :)

I appreciate your submissions very much!  Excellent work!  I have revised the brief to be more clear about what I think I'm looking for.  Keep the submissions coming in!!  Thank you so much :)

Target Market(s)

Wealthy home buyers and sellers in California.

Industry/Entity Type

Real Estate

Requirements
Must have
• Must include:

Homestead Partners Logo

Below Homestead Partners Logo it must say: Cedar Vale (Helvetica font)

Complete address: 58317 Marlow Street
Cedar Vale, CA 93428

Phone number: 805.492.1157 cell
805.374.2291 VM 5814 office

My photo

My name: Meg Horvath (please make sure it's correct before you submit) :)

My MH Logo (if possible please keep logo colors the same)

"Realtor" with a reserved symbol after or below my name

My license number: CalBRE #04827715

My website: www.MegHorvathHomes.example

My email: Meg@MegHorvathHomes.example

Nice to have
• I'm open minded :) The main goal is to have the MH logo is on all of my material. For the business cards I sort of imagine my MH logo in the background, and I like a fade. I prefer the logo to be on the front of the card, and I like it on the back of the card too, So a two sided business card is ok.

I prefer the light blue Homestead Partners Logo submitted. Please note the light blue color must closely match :)

Another idea is the business card can be in the format of the yard sign photo submitted (maybe changed into the light blue color), to possibly be a business card that looks like the yard sign. The yard sign layout must closely match the example submitted due to corporate guidelines.

Basically I'm looking for something that will tie everything together with my photo and logo so it's well branded in the clients mind. :)

Should not have
• Please keep the logo's exactly as they are, including color...no need to change.

If you choose to use the yard sign example provided for the business card, Please do not change the basic layout of the yard sign submitted, I have to follow the corporate standards.

```html
<!DOCTYPE html>
<html lang="en">
<head>
<meta charset="utf-8">
<title>Meg Horvath – Realtor Business Card</title>
<link rel="stylesheet" href="https://fonts.googleapis.com/css2?family=Arimo:wght@400;700&family=Montserrat:wght@600;700&display=swap">
<style>
  :root {
    --card-blue: #1a5aa8;
    --band-blue: #1857a4;
    --text-white: #ffffff;
    --text-blue: #1c5aa6;
    --gold-light: #ffe7a0;
    --gold-mid: #ffcd05;
    --gold-deep: #e3aa1e;
    --stripe-grey: #b9bec6;
    --stripe-white: #f4f6f9;
    --photo-top: #d9c9a8;
    --photo-bottom: #2a2a30;
  }
  html, body {
    margin: 0;
    padding: 0;
    overflow: hidden;
    background: #ffffff;
  }
  .card {
    position: relative;
    width: 1200px;
    height: 699px;
    overflow: hidden;
    background: var(--card-blue);
    font-family: "Arimo", Helvetica, Arial, sans-serif;
    color: var(--text-white);
  }
  .agent-photo {
    position: absolute;
    left: 709px;
    top: 95px;
    width: 391px;
    height: 400px;
    background: linear-gradient(180deg, var(--photo-top) 0%, #c8a982 45%, var(--photo-bottom) 100%);
    border-radius: 190px 190px 0 0;
  }
  .swoosh {
    position: absolute;
    left: 0;
    top: 0;
    width: 1200px;
    height: 699px;
  }
  .bottom-band {
    position: absolute;
    left: 0;
    bottom: 0;
    width: 1200px;
    height: 38px;
    background: var(--band-blue);
  }
  .agent-brand {
    position: absolute;
    left: 107px;
    top: 220px;
    width: 200px;
    text-align: center;
  }
  .agent-name {
    font-family: "Montserrat", Arial, sans-serif;
    font-weight: 700;
    font-size: 23px;
    line-height: 1.1;
    white-space: nowrap;
    margin-left: -20px;
    margin-right: -20px;
  }
  .agent-title {
    font-family: "Montserrat", Arial, sans-serif;
    font-weight: 600;
    font-size: 16px;
    letter-spacing: 0.6px;
    margin-top: 1px;
    margin-left: 40px;
  }
  .agent-title sup { font-size: 8px; }
  .contact-list {
    position: absolute;
    left: 98px;
    top: 290px;
    margin: 0;
    padding: 0;
    list-style: none;
    font-size: 24px;
    line-height: 31.7px;
  }
  .website {
    position: absolute;
    left: 100px;
    top: 597px;
    font-weight: 700;
    font-size: 23px;
    color: var(--text-blue);
  }
  .brokerage {
    position: absolute;
    left: 945px;
    top: 485px;
    width: 156px;
    height: 106px;
    display: flex;
    align-items: center;
    justify-content: center;
    text-align: center;
  }
  .brokerage-name {
    font-weight: 700;
    font-size: 21px;
    line-height: 1.15;
    color: var(--text-blue);
  }
  .brokerage-office {
    position: absolute;
    left: 935px;
    top: 597px;
    width: 176px;
    text-align: center;
    font-size: 23px;
    color: var(--text-blue);
  }
</style>
</head>
<body>
  <div class="card">
    <div class="agent-photo" role="img" aria-label="Portrait photo of Meg Horvath"></div>

    <svg class="swoosh" viewBox="0 0 1200 699" aria-hidden="true">
      <defs>
        <linearGradient id="gold" x1="0" y1="0" x2="1" y2="0">
          <stop offset="0" stop-color="var(--gold-light)"/>
          <stop offset="0.55" stop-color="var(--gold-mid)"/>
          <stop offset="1" stop-color="var(--gold-deep)"/>
        </linearGradient>
        <linearGradient id="stripe" x1="0" y1="0" x2="1" y2="0">
          <stop offset="0" stop-color="var(--stripe-grey)"/>
          <stop offset="0.6" stop-color="var(--stripe-white)"/>
          <stop offset="1" stop-color="var(--stripe-white)"/>
        </linearGradient>
      </defs>
      <path d="M0 512 C400 506 880 458 1200 350 L1200 699 L0 699 Z" fill="url(#stripe)"/>
      <path d="M0 531 C400 522 900 470 1200 365 L1200 699 L0 699 Z" fill="url(#gold)"/>
    </svg>

    <div class="bottom-band"></div>

    <div class="agent-brand">
      <div class="agent-name">Meg Horvath</div>
      <div class="agent-title">REALTOR<sup>®</sup></div>
    </div>

    <ul class="contact-list">
      <li>CalBRE #04827715</li>
      <li>Meg@MegHorvathHomes.example</li>
      <li>805.492.1157 Cell</li>
      <li>805.374.2291 VM 5814 Office</li>
      <li>58317 Marlow Street,</li>
      <li>Cedar Vale, CA 93428</li>
    </ul>

    <div class="website">www.MegHorvathHomes.example</div>

    <div class="brokerage">
      <span class="brokerage-name">Homestead<br>Partners</span>
    </div>
    <div class="brokerage-office">Cedar Vale</div>
  </div>
</body>
</html>
```